business card design for luxurious real estate brand

using the attached logo, i am looking for a 2-sided business card design. the back should be the gold logo on black background. the front needs to include: gold logo, name, phone, email, and website

Industry/Entity Type

real estate

Contact Information for Business Card

logo, name, email, phone, website

Font styles to use
Sans Serif

```html
<!DOCTYPE html>
<html lang="en">
<head>
<meta charset="utf-8">
<title>Casa Verano – Business Card</title>
<link rel="stylesheet" href="https://fonts.googleapis.com/css2?family=Open+Sans:wght@400;600&family=Arimo:wght@400&display=swap">
<style>
  :root {
    --stage: #3b3b3b;
    --paper: #ffffff;
    --ink: #1e1e1c;
    --gold: #fdcd00;
  }
  * { margin: 0; padding: 0; box-sizing: border-box; }
  html, body {
    width: 1200px;
    height: 1000px;
    overflow: hidden;
    background: var(--stage);
  }
  .card {
    position: absolute;
    left: 139px;
    top: 243px;
    width: 922px;
    height: 513px;
    background: var(--paper);
    overflow: hidden;
  }
  .card-shapes {
    position: absolute;
    inset: 0;
    width: 100%;
    height: 100%;
  }
  .brand-title {
    position: absolute;
    left: 75px;
    top: 62px;
    font-family: "Open Sans", sans-serif;
    font-weight: 400;
    font-size: 50px;
    line-height: 1;
    color: #111;
    letter-spacing: -0.5px;
  }
  .role {
    position: absolute;
    left: 231px;
    top: 141px;
    transform: translate(-50%, -50%);
    font-family: "Arimo", sans-serif;
    font-size: 20px;
    color: #111;
  }
  .contact {
    position: absolute;
    font-family: "Arimo", sans-serif;
    font-size: 17px;
    color: #111;
    transform: translateY(-50%);
    white-space: nowrap;
  }
  .contact-phone { left: 85px; top: 369px; }
  .contact-email { left: 85px; top: 415px; }
  .contact-web   { left: 300px; top: 416px; }
  .back-name {
    position: absolute;
    left: 743px;
    top: 285px;
    transform: translate(-50%, -50%);
    font-family: "Open Sans", sans-serif;
    font-weight: 600;
    font-size: 25px;
    letter-spacing: 6px;
    color: var(--gold);
    white-space: nowrap;
  }
</style>
</head>
<body>
  <div class="card">
    <svg class="card-shapes" viewBox="0 0 1614 897" preserveAspectRatio="none" aria-hidden="true">
      <!-- gold band -->
      <polygon fill="var(--gold)" points="974,0 1117,0 904,574 1214,897 1057,897 822,489"/>
      <!-- dark panel -->
      <polygon fill="var(--ink)" points="1117,0 1614,0 1614,897 1214,897 904,574"/>
      <!-- outline strokes -->
      <polyline fill="none" stroke="var(--ink)" stroke-width="6" points="929,2 774,490 1167,894"/>
      <polyline fill="none" stroke="var(--ink)" stroke-width="6" points="1067,4 814,699 1014,894"/>
      <!-- top accent stripes -->
      <polygon fill="var(--gold)" points="1192,0 1247,0 1317,56 1257,56"/>
      <polygon fill="var(--gold)" points="1254,0 1297,0 1362,56 1317,56"/>
      <!-- bottom accent stripes -->
      <polygon fill="var(--gold)" points="538,822 595,822 672,897 615,897"/>
      <polygon fill="var(--gold)" points="621,822 677,822 755,897 697,897"/>
      <!-- left pointer -->
      <polygon fill="var(--gold)" points="0,114 90,164 0,216"/>
      <!-- role arrows -->
      <polygon fill="var(--gold)" points="267,251 307,241 307,261"/>
      <polygon fill="var(--gold)" points="501,241 542,251 501,261"/>
      <!-- phone icon -->
      <path fill="var(--gold)" d="M100,624 C76,632 78,668 124,674 L120,666 C98,664 92,644 104,634 Z"/>
      <!-- mail icon -->
      <rect x="82" y="709" width="50" height="35" fill="var(--gold)"/>
      <polyline fill="none" stroke="var(--paper)" stroke-width="3" points="82,711 107,730 132,711"/>
      <polyline fill="none" stroke="var(--paper)" stroke-width="2" points="84,742 101,726 M130,742 113,726"/>
      <line x1="84" y1="742" x2="101" y2="726" stroke="var(--paper)" stroke-width="2"/>
      <line x1="130" y1="742" x2="113" y2="726" stroke="var(--paper)" stroke-width="2"/>
      <!-- globe icon -->
      <g fill="none" stroke="var(--gold)" stroke-width="4">
        <circle cx="490" cy="724" r="23"/>
        <ellipse cx="490" cy="724" rx="10" ry="23"/>
        <line x1="490" y1="701" x2="490" y2="747"/>
        <line x1="467" y1="724" x2="513" y2="724"/>
        <line x1="471" y1="712" x2="509" y2="712"/>
        <line x1="471" y1="736" x2="509" y2="736"/>
      </g>
    </svg>

    <h1 class="brand-title">CASA VERANO</h1>
    <p class="role">Manager</p>
    <p class="contact contact-phone">+1555014229874</p>
    <p class="contact contact-email">Casa@Mailbox.com</p>
    <p class="contact contact-web">www.casaverano.com</p>

    <p class="back-name">CASA VERANO</p>
  </div>
</body>
</html>
```